Flyer for Fertility Specialty Pharmacy

We need to design a flyer , which contains the information about our Fertility Pharmacy , Services, and Medication pricing. We will be distributing these to Fertility clinics and Patients. We will provide the logo.
http://corvelmedrx.com/

Target Market(s)

Fertility Clinics , IVF patients, Other pharmacies

Industry/Entity Type

Fertility

Requirements
Must have
• baby pictures , or related to Fertility, IVF etc
Nice to have
• This flyer is to attract couples who are trying for pregnancy.

```html
<!DOCTYPE html>
<html lang="en">
<head>
<meta charset="utf-8">
<title>Halden's Crestview Pharmacy – Fertility Pricing Brochure</title>
<link href="https://fonts.googleapis.com/css2?family=Barlow+Condensed:wght@600;700;800&family=Barlow:wght@400;500;600;700&display=swap" rel="stylesheet">
<style>
  :root{
    --green:#10a888;
    --green-dark:#0c8f74;
    --green-text:#0e9a7d;
    --white:#ffffff;
    --ink:#1d2a2a;
    --gold:#d9b54a;
    --bg:#d9dcdc;
  }
  *{box-sizing:border-box;margin:0;padding:0}
  html,body{width:1200px;height:900px;overflow:hidden;background:var(--bg)}
  body{font-family:'Barlow',sans-serif;color:var(--white)}
  .brochure{display:flex;width:1200px;height:900px}
  .panel{position:relative;width:400px;height:900px;overflow:hidden}
  .panel--green{background:var(--green)}
  .panel--white{background:var(--white)}
  .cap{position:absolute;top:0;left:0;width:400px;height:110px}
  .cap-label{position:absolute;top:28px;left:0;width:100%;text-align:center;font-size:12px;line-height:1.15;letter-spacing:.5px;text-transform:uppercase;font-weight:500}
  .cap-label--green{color:var(--green-text)}
  .cap-label--white{color:var(--white)}
  .heading{font-family:'Barlow Condensed',sans-serif;font-weight:800;text-transform:uppercase;line-height:1}
  .heading-rule{height:2px;background:currentColor;margin-top:6px}

  /* pricing panel */
  .pricing{position:absolute;top:120px;left:42px;right:36px}
  .pricing .heading{font-size:48px}
  .med-list{list-style:none;margin-top:10px;font-size:14.5px;line-height:17px}
  .med-list li{display:flex;justify-content:space-between}
  .med-list .price{width:50px;font-size:13px}
  .services{position:absolute;top:500px;left:42px;right:30px}
  .services .heading{font-size:52px}
  .service-list{list-style:none;margin-top:14px;font-size:16px;line-height:19px}
  .service-list li{display:flex;gap:12px;margin-bottom:7px}
  .tick{flex:0 0 22px;height:22px;margin-top:1px}

  /* bundle panel */
  .bundle{position:absolute;top:128px;left:44px;right:40px;color:var(--green-text)}
  .bundle .heading{font-size:50px}
  .bundle-head{display:flex;justify-content:space-between;align-items:flex-end;margin-top:14px;font-weight:700;font-size:15px}
  .bundle-head span{border-bottom:2px solid var(--green-text);padding-bottom:2px}
  .bundle-list{list-style:none;margin-top:8px;font-weight:700;font-size:16px;line-height:18px}
  .bundle-kit{margin-top:16px;font-weight:700;font-size:16px}
  .bundle-note{margin-top:12px;font-weight:600;font-size:21px}
  .badge{display:block;margin:16px auto 0;width:180px;height:180px}
  .accredit{text-align:center;color:var(--ink);margin-top:6px}
  .accredit-title{font-weight:700;font-size:22px;letter-spacing:2px;color:#1f3a55}
  .accredit-sub{font-size:20px;line-height:23px}
  .program{position:absolute;left:30px;right:30px;bottom:40px;height:150px;background:var(--green);border-radius:34px 34px 0 0;display:flex;align-items:center;justify-content:center;text-align:center}
  .program .heading{font-size:38px;line-height:1.1;color:var(--white)}

  /* contact panel */
  .brand{position:absolute;top:135px;left:40px;display:flex;align-items:center;gap:16px}
  .brand-mark{flex:0 0 40px;width:40px;height:40px;border-radius:50%;background:var(--white)}
  .brand-name{font-weight:700;font-size:30px;line-height:32px}
  .address{position:absolute;top:245px;left:40px;font-style:normal;font-weight:700;font-size:25px;line-height:30px}
  .contacts{position:absolute;top:355px;left:40px;list-style:none;font-weight:600;font-size:28px;line-height:40px}
  .contacts li{display:flex;align-items:center;gap:16px}
  .contacts svg{width:28px;height:28px}
  .shipping-art{position:absolute;left:0;right:0;bottom:0;height:400px;background:linear-gradient(180deg,#13ad8c 0%,#0c9477 100%)}
  .pill{position:absolute;background:var(--white);color:var(--green-text);font-family:'Barlow Condensed',sans-serif;font-weight:700;font-size:28px;padding:4px 26px;border-radius:20px}
  .pill--free{top:560px;left:40px;border-radius:0 20px 20px 0;padding-left:30px}
  .pill--ship{top:760px;right:30px}
</style>
</head>
<body>
<main class="brochure">

  <!-- Pricing & services -->
  <section class="panel panel--green">
    <svg class="cap" viewBox="0 0 400 110" aria-hidden="true"><path d="M0 0H400V70Q220 70 180 95Q150 110 0 110Z" fill="#fff"/></svg>
    <p class="cap-label cap-label--green">Confidential pricing for CFRC<br>Colorado</p>
    <div class="pricing">
      <h2 class="heading">Medications</h2>
      <div class="heading-rule"></div>
      <ul class="med-list">
        <li><span>Progesterone 100mg capsule each</span><span class="price">$ 0.00</span></li>
        <li><span>Progesterone 200mg capsule each</span><span class="price">$ 2.00</span></li>
        <li><span>Lutavel 8% (per applicator)</span><span class="price">$</span></li>
        <li><span>Progesterone in Oil 50mg/ml</span><span class="price">$</span></li>
        <li><span>Chorigen 5,000 units</span><span class="price">$</span></li>
        <li><span>Ganirelix 250mcg PFS</span><span class="price"></span></li>
        <li><span>Menofolin 75</span><span class="price">$</span></li>
        <li><span>Gonavex 10,000 units</span><span class="price"></span></li>
        <li><span>Cetrolix 250mcg</span><span class="price"></span></li>
        <li><span>Follira 300</span><span class="price">$</span></li>
        <li><span>Follira 600</span><span class="price">$9</span></li>
        <li><span>Follira 900</span><span class="price"></span></li>
        <li><span>Endovira 100mg</span><span class="price"></span></li>
        <li><span>Ovulex 250mcg PFS</span><span class="price"></span></li>
        <li><span>Leuprolide 2-week kit</span><span class="price"></span></li>
      </ul>
    </div>
    <div class="services">
      <h2 class="heading">Services</h2>
      <div class="heading-rule"></div>
      <ul class="service-list">
        <li><svg class="tick" viewBox="0 0 22 22"><circle cx="11" cy="11" r="9" fill="none" stroke="#fff" stroke-width="2"/><path d="M6 11l4 4 9-10" fill="none" stroke="#fff" stroke-width="2.4"/></svg><span>Fertility specialist Pharmacist on call 24/7</span></li>
        <li><svg class="tick" viewBox="0 0 22 22"><circle cx="11" cy="11" r="9" fill="none" stroke="#fff" stroke-width="2"/><path d="M6 11l4 4 9-10" fill="none" stroke="#fff" stroke-width="2.4"/></svg><span>Personal service to all patients</span></li>
        <li><svg class="tick" viewBox="0 0 22 22"><circle cx="11" cy="11" r="9" fill="none" stroke="#fff" stroke-width="2"/><path d="M6 11l4 4 9-10" fill="none" stroke="#fff" stroke-width="2.4"/></svg><span>Individual counseling provided for all the patients</span></li>
        <li><svg class="tick" viewBox="0 0 22 22"><circle cx="11" cy="11" r="9" fill="none" stroke="#fff" stroke-width="2"/><path d="M6 11l4 4 9-10" fill="none" stroke="#fff" stroke-width="2.4"/></svg><span>Once the patient leaves your office the rest is on us</span></li>
        <li><svg class="tick" viewBox="0 0 22 22"><circle cx="11" cy="11" r="9" fill="none" stroke="#fff" stroke-width="2"/><path d="M6 11l4 4 9-10" fill="none" stroke="#fff" stroke-width="2.4"/></svg><span>Initiate and follow up on the prior authorizations.</span></li>
        <li><svg class="tick" viewBox="0 0 22 22"><circle cx="11" cy="11" r="9" fill="none" stroke="#fff" stroke-width="2"/><path d="M6 11l4 4 9-10" fill="none" stroke="#fff" stroke-width="2.4"/></svg><span>We have all fertility medications in stock</span></li>
        <li><svg class="tick" viewBox="0 0 22 22"><circle cx="11" cy="11" r="9" fill="none" stroke="#fff" stroke-width="2"/><path d="M6 11l4 4 9-10" fill="none" stroke="#fff" stroke-width="2.4"/></svg><span>Free next day delivery via ParcelJet to Home or work</span></li>
      </ul>
    </div>
  </section>

  <!-- IVF bundle -->
  <section class="panel panel--white">
    <svg class="cap" viewBox="0 0 400 110" aria-hidden="true"><path d="M0 0H400V70Q220 70 180 95Q150 110 0 110Z" fill="#10a888"/></svg>
    <p class="cap-label cap-label--white">Confidential pricing for CFRC<br>Colorado</p>
    <div class="bundle">
      <h2 class="heading">IVF Bundle</h2>
      <div class="heading-rule"></div>
      <div class="bundle-head"><span>Medication name</span><span>Quantity</span></div>
      <ul class="bundle-list">
        <li>Endovira</li>
        <li>Progesterone 200mg caps</li>
        <li>Ganirelix 250mcg PFS</li>
        <li>Follira 300</li>
        <li>Gonavex</li>
      </ul>
      <p class="bundle-kit">Leuprolide Kit</p>
      <p class="bundle-note">For the above IVF Bundle:</p>
      <svg class="badge" viewBox="0 0 180 180" role="img" aria-label="Accreditation badge">
        <circle cx="90" cy="90" r="86" fill="var(--gold)"/>
        <circle cx="90" cy="90" r="70" fill="#fff"/>
      </svg>
      <div class="accredit">
        <p class="accredit-title">ACCREDITED</p>
        <p class="accredit-sub">Specialty Pharmacy<br>Expires 06/01/2024</p>
      </div>
    </div>
    <div class="program"><p class="heading">We are a Renew RX<br>&amp; Hope Program</p></div>
  </section>

  <!-- Contact -->
  <section class="panel panel--green">
    <svg class="cap" viewBox="0 0 400 110" aria-hidden="true"><path d="M0 0H400V60Q250 60 200 80Q150 100 0 100Z" fill="#fff"/></svg>
    <p class="cap-label cap-label--green">Confidential pricing for CFRC<br>Colorado</p>
    <div class="brand">
      <span class="brand-mark"></span>
      <p class="brand-name">Halden's<br>Crestview Pharmacy</p>
    </div>
    <address class="address">245 Linden Grove<br>Meadowbrook Road<br>Fairview, NJ 08999</address>
    <div class="shipping-art" role="img" aria-label="Delivery truck illustration for free shipping"></div>
    <ul class="contacts">
      <li><svg viewBox="0 0 24 24"><path d="M6 3l3 4-2 2c1 3 4 6 7 7l2-2 4 3-2 4C10 21 3 14 3 5z" fill="none" stroke="#fff" stroke-width="1.8" stroke-linejoin="round"/></svg>555-201-7300</li>
      <li><svg viewBox="0 0 24 24"><rect x="7" y="2" width="10" height="20" rx="2" fill="none" stroke="#fff" stroke-width="1.8"/><circle cx="12" cy="18" r="1.2" fill="#fff"/></svg>555-310-4410</li>
      <li><svg viewBox="0 0 24 24"><rect x="7" y="3" width="10" height="6" fill="none" stroke="#fff" stroke-width="1.8"/><rect x="3" y="9" width="18" height="8" rx="1" fill="none" stroke="#fff" stroke-width="1.8"/><rect x="7" y="14" width="10" height="7" fill="none" stroke="#fff" stroke-width="1.8"/></svg>555-482-9060</li>
    </ul>
    <span class="pill pill--free">Free</span>
    <span class="pill pill--ship">Shipping</span>
  </section>

</main>
</body>
</html>
```